Tall Oak Grove Transportation Management Association

We are looking to design an awards certificate for an upcoming event that we are having in December. This award would be given to our employee members who have done an outstanding job of promoting commuting alternatives (biking, walking, transit, ridesharing) to driving alone, and as such have reduced green house gas emissions. We are looking for a cool graphic that will make the award something special and worth framing. Attached is our current logo which should be on the certificate somewhere, as well as a few of our program design logos which can be used for inspiration.

Target Market(s)

Board members

Industry/Entity Type

Event

Requirements
Must have
• Graphic suitable for framing as part of an awards certificate
Nice to have
• Something that relates to what we do which is promoting sustainable tranportation (biking, walking, transit, and ridesharing).

```html
<!DOCTYPE html>
<html lang="en">
<head>
<meta charset="utf-8">
<title>Award Certificate – Tall Oak Grove TMA</title>
<link href="https://fonts.googleapis.com/css2?family=Tinos:wght@400;700&family=Ubuntu:wght@400;500&display=swap" rel="stylesheet">
<style>
  :root {
    --teal: #1aa3a0;
    --blue: #1b86c4;
    --paper: #f4f2ea;
    --paper-edge: #d9d3c2;
    --ink: #111111;
    --green: #6fae4a;
    --red: #ee6a4c;
    --sky: #4fb0dd;
    --orange: #f5a232;
    --aqua: #46b6c6;
    --olive: #9ab03e;
    --grey: #8a8a8a;
  }
  * { margin: 0; padding: 0; box-sizing: border-box; }
  html, body { width: 1200px; height: 927px; overflow: hidden; background: #ffffff; }
  .certificate { position: relative; width: 1200px; height: 927px; font-family: "Tinos", "Times New Roman", serif; color: var(--ink); }
  .frame-ornament {
    position: absolute; inset: 0;
    background: linear-gradient(135deg, var(--teal) 0%, var(--blue) 45%, var(--teal) 100%);
    border-radius: 6px;
  }
  .paper {
    position: absolute; left: 76px; top: 60px; width: 1052px; height: 805px;
    background: radial-gradient(ellipse at center, #f8f7f2 55%, var(--paper) 80%, var(--paper-edge) 100%);
    box-shadow: inset 0 0 18px rgba(120,110,90,.35);
  }
  .title {
    position: absolute; left: 0; width: 1200px; top: 138px; text-align: center;
    font-weight: 700; font-size: 96px; letter-spacing: 1px; line-height: 1;
    background: linear-gradient(90deg, var(--teal), var(--blue));
    -webkit-background-clip: text; background-clip: text; color: transparent;
  }
  .presented {
    position: absolute; left: 0; width: 1200px; top: 248px; text-align: center;
    font-size: 19px; letter-spacing: 2.4px;
  }
  .name-line { position: absolute; left: 218px; top: 359px; width: 786px; border-top: 1.5px solid var(--ink); }
  .citation {
    position: absolute; left: 218px; top: 378px; width: 786px; text-align: center;
    font-size: 21px; line-height: 26px;
  }
  .programs-art {
    position: absolute; left: 232px; top: 450px; width: 752px; height: 58px;
    background: linear-gradient(90deg, rgba(111,174,74,.35), rgba(238,106,76,.35), rgba(79,176,221,.35), rgba(245,162,50,.35), rgba(70,182,198,.35), rgba(154,176,62,.35));
    border-radius: 6px;
  }
  .programs {
    position: absolute; left: 220px; top: 512px; width: 776px;
    display: flex; justify-content: space-between;
    font-family: "Ubuntu", sans-serif; font-size: 15.5px; font-weight: 500;
  }
  .programs .p-ride-home { color: var(--green); }
  .programs .p-matching { color: var(--red); }
  .programs .p-express { color: var(--sky); }
  .programs .p-carpool { color: var(--orange); }
  .programs .p-workout { color: var(--aqua); }
  .programs .p-vanpool { color: var(--olive); }
  .ribbon {
    position: absolute; left: 76px; top: 616px; width: 1052px; height: 36px;
    background: linear-gradient(90deg, var(--teal), var(--blue) 50%, var(--blue));
    border-top: 2px solid #d7d93a;
  }
  .seal { position: absolute; left: 503px; top: 559px; width: 150px; height: 150px; }
  .field-label { position: absolute; top: 752px; font-size: 21px; }
  .field-line { position: absolute; top: 769px; border-top: 1.2px solid var(--ink); }
  .date-label { left: 158px; }
  .date-line { left: 208px; width: 236px; }
  .sign-label { left: 731px; }
  .sign-line { left: 822px; width: 226px; }
  .org-mark { position: absolute; left: 462px; top: 744px; width: 252px; text-align: center; color: var(--ink); }
  .org-mark .short { font-size: 40px; line-height: 44px; letter-spacing: -1px; }
  .org-mark .full { font-size: 9px; letter-spacing: .2px; margin-top: 6px; }
</style>
</head>
<body>
<main class="certificate">
  <div class="frame-ornament" role="img" aria-label="Ornate teal and blue scrollwork border framing the certificate"></div>
  <div class="paper"></div>

  <h1 class="title">CERTIFICATE</h1>
  <p class="presented">THIS CERTIFICATE IS PRESENTED TO</p>
  <div class="name-line"></div>
  <p class="citation">Lorem ipsum dolor sit amet, consectetuer adipiscing elit. Aenean commodo ligula eget dolor.</p>

  <div class="programs-art" role="img" aria-label="Line drawings of commuting options: house and car, carpool, bus and ferry, carpoolers, walker and cyclist, vanpool"></div>
  <div class="programs">
    <span class="p-ride-home">guaranteed ride home</span>
    <span class="p-matching">ride matching</span>
    <span class="p-express">express yourself</span>
    <span class="p-carpool">carpool subsidy</span>
    <span class="p-workout">workout to work</span>
    <span class="p-vanpool">vanpool subsidy</span>
  </div>

  <div class="ribbon"></div>
  <svg class="seal" viewBox="0 0 150 150" aria-hidden="true">
    <defs>
      <linearGradient id="sealFill" x1="0" y1="0" x2="1" y2="1">
        <stop offset="0" stop-color="#1aa3a0"/>
        <stop offset="1" stop-color="#1b86c4"/>
      </linearGradient>
    </defs>
    <polygon fill="url(#sealFill)" points="75,2 83,12 95,5 99,17 112,14 112,27 125,28 121,40 133,45 125,55 135,63 124,70 131,81 119,85 123,97 110,97 111,110 98,107 95,120 84,114 75,124 66,114 55,120 52,107 39,110 40,97 27,97 31,85 19,81 26,70 15,63 25,55 17,45 29,40 25,28 38,27 38,14 51,17 55,5 67,12" transform="translate(0,13)"/>
    <circle cx="75" cy="75" r="50" fill="none" stroke="#ffffff" stroke-width="6" stroke-dasharray="5 3"/>
    <circle cx="75" cy="75" r="40" fill="url(#sealFill)"/>
  </svg>

  <span class="field-label date-label">Date</span>
  <div class="field-line date-line"></div>
  <span class="field-label sign-label">Signature</span>
  <div class="field-line sign-line"></div>

  <div class="org-mark">
    <div class="short">Tall Oak Grove TMA</div>
    <div class="full">Tall Oak Grove Transportation Management Association</div>
  </div>
</main>
</body>
</html>
```